BRISK SWEEP

Need a professional looking business card that can fit : Name, Title, Cell, and office phone numbers. On the flip side we would like a list of our services : Highway accident management and towing, Crime scene clean up, Illegal drug lab clean up, Drug disposal, and Hazardous materials clean up.

```html
<!DOCTYPE html>
<html lang="en">
<head>
<meta charset="utf-8">
<title>Brisk Sweep — Business Card</title>
<link href="https://fonts.googleapis.com/css2?family=Cinzel:wght@400;600;700&display=swap" rel="stylesheet">
<style>
  :root{
    --navy:#1d3658;
    --navy-ink:#1f3152;
    --gold:#e8b631;
    --red:#c8202f;
    --white:#ffffff;
    --page:#e9e6e1;
    --watermark:rgba(255,255,255,0.06);
  }
  *{margin:0;padding:0;box-sizing:border-box}
  html,body{width:1200px;height:1200px;overflow:hidden}
  body{
    background:var(--page);
    font-family:'Cinzel',serif;
    position:relative;
  }
  .card{
    position:absolute;
    left:170px;
    width:860px;
    height:490px;
    border-radius:40px;
    overflow:hidden;
    box-shadow:0 10px 30px rgba(0,0,0,0.18);
  }
  /* FRONT */
  .card-front{top:90px;background:var(--white)}
  .stripes{position:absolute;left:0;right:0;top:190px}
  .stripe-navy{height:9px;background:var(--navy)}
  .stripe-gap{height:5px}
  .stripe-gold{height:6px;background:var(--gold)}
  .brand-seal{
    position:absolute;left:60px;top:50px;
    width:300px;height:300px;border-radius:50%;
    background:var(--navy);
    border:8px solid var(--gold);
    box-shadow:0 0 0 4px var(--navy);
    display:flex;align-items:center;justify-content:center;
  }
  .brand-name{
    color:var(--gold);
    font-weight:700;
    font-size:40px;
    line-height:1.1;
    text-align:center;
    letter-spacing:1px;
  }
  .contact{position:absolute;left:445px;top:0;right:30px;bottom:0;color:var(--navy-ink)}
  .person-name{position:absolute;top:132px;left:0;font-size:38px;font-weight:700;line-height:1;letter-spacing:.5px;white-space:nowrap}
  .person-title{position:absolute;top:222px;left:0;font-size:24px;line-height:1;color:var(--gold);letter-spacing:1px}
  .address{position:absolute;top:262px;left:0;font-size:27px;line-height:1.2;white-space:nowrap}
  .lines{position:absolute;top:340px;left:0;list-style:none}
  .lines li{display:flex;align-items:center;gap:16px;font-size:26px;line-height:1.45;white-space:nowrap}
  .lines svg{width:28px;height:28px;flex:none}
  /* BACK */
  .card-back{top:620px;background:var(--navy)}
  .watermark{
    position:absolute;left:300px;top:85px;width:260px;height:260px;border-radius:50%;
    border:6px solid var(--watermark);
  }
  .services{position:absolute;left:70px;top:150px;list-style:none}
  .services li{color:var(--gold);font-size:28px;font-weight:600;line-height:1.1;letter-spacing:.3px;white-space:nowrap}
  .services li::before{content:"\2605";color:var(--red);margin-right:4px;font-family:sans-serif;font-size:24px}
</style>
</head>
<body>

<section class="card card-front">
  <div class="stripes">
    <div class="stripe-navy"></div>
    <div class="stripe-gap"></div>
    <div class="stripe-gold"></div>
  </div>
  <div class="brand-seal"><span class="brand-name">BRISK<br>SWEEP</span></div>
  <div class="contact">
    <h1 class="person-name">Daniel J Harper</h1>
    <p class="person-title">Principal</p>
    <p class="address">482 Maple Ridge Road<br>Charleston, WV 25314</p>
    <ul class="lines">
      <li>
        <svg viewBox="0 0 24 24" aria-hidden="true"><rect x="6" y="2" width="12" height="20" rx="2" fill="var(--navy)"/><rect x="8" y="5" width="8" height="12" fill="#fff"/></svg>
        (304) 555-0142
      </li>
      <li>
        <svg viewBox="0 0 24 24" aria-hidden="true"><rect x="2" y="3" width="6" height="19" rx="2" fill="var(--navy)"/><rect x="9" y="7" width="13" height="15" rx="1" fill="var(--navy)"/><g fill="#fff"><rect x="11" y="9" width="9" height="3"/><rect x="11" y="14" width="2" height="2"/><rect x="14.5" y="14" width="2" height="2"/><rect x="18" y="14" width="2" height="2"/><rect x="11" y="18" width="2" height="2"/><rect x="14.5" y="18" width="2" height="2"/><rect x="18" y="18" width="2" height="2"/></g></svg>
        (304) 555-0178
      </li>
      <li>
        <svg viewBox="0 0 24 24" aria-hidden="true"><rect x="1" y="5" width="22" height="15" rx="1" fill="var(--navy)"/><path d="M2 6l10 8 10-8" fill="none" stroke="#fff" stroke-width="1.6"/></svg>
        hello@brisksweep.com
      </li>
    </ul>
  </div>
</section>

<section class="card card-back">
  <div class="watermark" aria-hidden="true"></div>
  <ul class="services">
    <li>Highway accident management and towing</li>
    <li>Crime scene clean up</li>
    <li>Illegal drug lab clean up</li>
    <li>Drug disposal and</li>
    <li>Hazardous materials clean up</li>
  </ul>
</section>

</body>
</html>
```